Creative Business Card for my Sail Boat.. Tide & Time

Going to order PLASTIC business cards for my boat.. she is a sailing vessel catamaran named Tide & Time..

Target Market(s)

to impress other boaters with a unique designed plastic card

Contact Information for Business Card

S/V Tide & Time
Captain Tom Harlow
harlow@tom.example
Mobile/WhatsApp 1-555-318-7062
www.sailtideandtime.example

Requirements
Must have
• Cool colors. logo.. and info in Business Card Details.. Thanks! Utilize clear or cloudy plastic in design. Thanks

```html
<!DOCTYPE html>
<html lang="en">
<head>
<meta charset="utf-8">
<title>Tide &amp; Time – Business Card</title>
<link href="https://fonts.googleapis.com/css2?family=Arimo:wght@400;700&display=swap" rel="stylesheet">
<style>
  :root {
    --backdrop: #1b1b1c;
    --frost: #8e9092;
    --frost-light: #a3a5a7;
    --sail-green: #3f9a4c;
    --wake-red: #c8353a;
    --label-green: #4fb04f;
    --name-white: #f2f2f2;
    --detail-white: #e6e6e6;
    --brand-sand: #d9cbc1;
  }
  html, body {
    margin: 0;
    width: 1200px;
    height: 800px;
    overflow: hidden;
    background: var(--backdrop);
    font-family: "Arimo", Arial, sans-serif;
  }
  .business-card {
    position: absolute;
    left: 100px;
    top: 90px;
    width: 1000px;
    height: 620px;
    border-radius: 40px;
    overflow: hidden;
    background: linear-gradient(160deg, var(--frost-light), var(--frost));
    box-shadow: inset 0 0 0 3px rgba(255,255,255,0.25);
  }
  .card-art {
    position: absolute;
    inset: 0;
    width: 100%;
    height: 100%;
  }
  .card-content {
    position: absolute;
    left: 0;
    right: 0;
    top: 150px;
    text-align: center;
    padding-left: 110px;
  }
  .brand-mark {
    display: inline-flex;
    align-items: center;
    gap: 18px;
    margin-bottom: 34px;
  }
  .brand-name {
    font-weight: 700;
    font-size: 76px;
    color: var(--brand-sand);
    letter-spacing: 1px;
  }
  .brand-dot {
    width: 34px;
    height: 34px;
    border-radius: 50%;
    background: var(--sail-green);
  }
  .captain-name {
    margin: 0 0 22px;
    font-weight: 700;
    font-size: 52px;
    color: var(--name-white);
  }
  .contact-list {
    margin: 0;
    padding: 0;
    list-style: none;
    font-size: 28px;
    line-height: 1.35;
    color: var(--detail-white);
  }
  .contact-label {
    font-weight: 700;
    color: var(--label-green);
  }
</style>
</head>
<body>
  <div class="business-card">
    <svg class="card-art" viewBox="0 0 1000 620" preserveAspectRatio="none" aria-hidden="true">
      <path d="M0,0 H560 Q180,60 0,250 Z" fill="var(--sail-green)"/>
      <path d="M0,250 Q180,60 560,0 L610,0 Q200,52 0,266 Z" fill="var(--wake-red)"/>
      <path d="M1000,620 H430 Q820,570 1000,360 Z" fill="var(--sail-green)"/>
      <path d="M1000,360 Q820,570 430,620 L390,620 Q805,562 1000,340 Z" fill="var(--wake-red)"/>
    </svg>
    <div class="card-content">
      <div class="brand-mark">
        <span class="brand-name">Tide &amp; Time</span>
        <span class="brand-dot"></span>
      </div>
      <h1 class="captain-name">Captain Tom Harlow</h1>
      <ul class="contact-list">
        <li><span class="contact-label">WhatsApp:</span> 1-555-318-7062</li>
        <li><span class="contact-label">Email:</span> harlow@tom.example</li>
        <li><span class="contact-label">Web:</span> www.sailtideandtime.example</li>
      </ul>
    </div>
  </div>
</body>
</html>
```